English and Spanish Language School Needs a Business Card

Need a business card design a startup company called Corvelle Language School. The company will offer English and Spanish conversational level courses designed to make the learner feel comfortable with grammar and vocabulary. We would like to see a logo with some colour that should communicate learning, growth.

Target Market(s)

Consumers and businesses

Industry/Entity Type

Education

Contact Information for Business Card

TBD

Font styles to use
Serif

Requirements
Must have
• Include the following
• Logo
• Name
• Title
• Cellphone Number
• Office Phone number
• Email address
• Office Address

```html
<!DOCTYPE html>
<html lang="en">
<head>
<meta charset="utf-8">
<title>Corvelle Language School – Business Card</title>
<link rel="stylesheet" href="https://fonts.googleapis.com/css2?family=Source+Sans+3:wght@400;600;700&display=swap">
<style>
  :root {
    --page-bg: #e9e6e3;
    --card-red: #9b2426;
    --card-black: #111111;
    --brand-teal: #13a0a8;
    --brand-red: #d7232f;
    --text-light: #ffffff;
  }
  * { margin: 0; padding: 0; box-sizing: border-box; }
  html, body {
    width: 1200px; height: 900px; overflow: hidden;
    background: var(--page-bg);
    font-family: "Source Sans 3", "Myriad Pro", Arial, sans-serif;
  }
  .canvas { position: relative; width: 1200px; height: 900px; }

  .card {
    position: absolute;
    width: 556px; height: 343px;
    overflow: hidden;
    box-shadow: 0 6px 18px rgba(0,0,0,.18);
  }
  .card--front { left: 238px; top: 61px; background: var(--card-red); }
  .card--back  { left: 457px; top: 518px; width: 560px; background: var(--card-black); }

  .card__split { position: absolute; inset: 0; width: 100%; height: 100%; }

  .contact {
    position: absolute; left: 49px; top: 73px;
    color: var(--text-light);
  }
  .contact__name { font-size: 21px; font-weight: 700; line-height: 1.1; }
  .contact__title { font-size: 16px; font-weight: 400; margin-top: 3px; }
  .contact__list { list-style: none; margin-top: 26px; font-size: 15.5px; line-height: 21.5px; }
  .contact__list li { display: flex; align-items: center; gap: 6px; }
  .contact__icon { width: 11px; height: 11px; fill: var(--text-light); flex: none; }
  .contact__address { font-size: 15.5px; line-height: 22px; margin-top: 20px; font-style: normal; }

  .brand { position: absolute; font-weight: 600; line-height: 1; }
  .brand--small {
    right: 36px; top: 238px; color: var(--brand-teal); text-align: left;
  }
  .brand--small .brand__word { font-size: 40px; letter-spacing: -0.5px; }
  .brand--small .brand__sub  { font-size: 13.5px; margin-top: 2px; padding-left: 12px; }

  .brand--large {
    left: 0; right: 0; top: 112px; text-align: center; color: var(--brand-red);
  }
  .brand--large .brand__word { font-size: 86px; letter-spacing: -1px; }
  .brand--large .brand__sub  { font-size: 24px; margin-top: 4px; }
</style>
</head>
<body>
<main class="canvas">

  <section class="card card--front" aria-label="Business card front">
    <svg class="card__split" viewBox="0 0 556 343" preserveAspectRatio="none" aria-hidden="true">
      <polygon points="490,0 556,0 556,343 267,343" fill="var(--card-black)"/>
    </svg>

    <div class="contact">
      <p class="contact__name">Mathieu Lavallée</p>
      <p class="contact__title">President</p>
      <ul class="contact__list">
        <li>
          <svg class="contact__icon" viewBox="0 0 24 24" aria-hidden="true"><path d="M6.6 10.8c1.4 2.8 3.8 5.1 6.6 6.6l2.2-2.2c.3-.3.7-.4 1-.2 1.1.4 2.3.6 3.6.6.6 0 1 .4 1 1V20c0 .6-.4 1-1 1C10.6 21 3 13.4 3 4c0-.6.4-1 1-1h3.5c.6 0 1 .4 1 1 0 1.3.2 2.5.6 3.6.1.3 0 .7-.2 1z"/></svg>
          438-2917-054
        </li>
        <li>
          <svg class="contact__icon" viewBox="0 0 24 24" aria-hidden="true"><path d="M2 8c3-4 17-4 20 0l-1 3h-4l-1-3H8l-1 3H3zM5 13h14l1 8H4zM12 14.5a2.5 2.5 0 1 0 0 5 2.5 2.5 0 0 0 0-5z"/></svg>
          (514)555-0182
        </li>
        <li>
          <svg class="contact__icon" viewBox="0 0 24 24" aria-hidden="true"><path d="M2 5h20v14H2zM3.5 6.5 12 13l8.5-6.5v-.5h-17z"/></svg>
          info@corvelleschool.com
        </li>
      </ul>
      <address class="contact__address">4275 Rue des Érables<br>Laval, QC, H7N2K4</address>
    </div>

    <div class="brand brand--small">
      <p class="brand__word">Corvelle</p>
      <p class="brand__sub">Language School</p>
    </div>
  </section>

  <section class="card card--back" aria-label="Business card back">
    <div class="brand brand--large">
      <p class="brand__word">Corvelle</p>
      <p class="brand__sub">Language School</p>
    </div>
  </section>

</main>
</body>
</html>
```